Brindle Industries - Quality Campaign

Objective:

Create a visually engaging graphic design that promotes quality awareness and engagement within Brindle Industries. The design should convey the core values of quality at Brindle, emphasizing its four key elements:

Zero Defects, Zero Scrap
Customer Satisfaction
First Time Right
Product Performance
Target Audience:

Brindle Industries employees at all levels.

Usage:

The design will be used for various purposes, including:

Posters displayed in common areas and workstations
Presentation slides for internal meetings and training sessions
Design Requirements:

Visual Style: The design should be modern, professional, and visually appealing. It should evoke a sense of pride in quality and inspire team members to strive for excellence.
Color Palette: Consider using the Brindle Industries brand colors or a complementary palette that reflects quality and professionalism (see website: https://www.brindle-industries.example/).
Key Elements: The four key elements of quality should be clearly visible and integrated into the design. This could be achieved through text, icons, or a combination of both.
Brindle Industries Logo: A vector file of the Brindle Industries logo will be provided. Optional use of the logo is encouraged to maintain brand consistency.
Call to Action: The design should include a clear call to action, such as "Embrace Quality," "Strive for Excellence," or "Own Your Quality."
Additional Considerations:

Versatility: The design should be adaptable for different formats and sizes (e.g., posters, presentations, social media posts).
Memorability: The design should be memorable and easily recognizable as representing Brindle Industries' commitment to quality.
Deliverables:

High-resolution digital files in various formats suitable for printing and digital use.
By adhering to these guidelines, the winning design will effectively communicate the importance of quality at Brindle Industries and inspire employees to embrace these values in their daily work.

Industry/Entity Type

Engineering, manufacturing, semi-conductor, optics

Requirements
Must have
• Reference to Quality and 4 key elements

```html
<!DOCTYPE html>
<html lang="en">
<head>
<meta charset="UTF-8">
<title>Brindle Industries – The Core Values of Quality</title>
<link rel="stylesheet" href="https://fonts.googleapis.com/css2?family=Arimo:wght@400;700&family=Roboto:wght@400&display=swap">
<style>
  :root {
    --stage: #b3b3b3;
    --paper: #ffffff;
    --ink: #050608;
    --accent-blue: #4d87c8;
    --photo-light: #f1ede0;
    --photo-mid: #d9d6cf;
    --photo-dark: #5a5a62;
    --text-white: #ffffff;
  }
  * { box-sizing: border-box; margin: 0; padding: 0; }
  html, body { width: 1200px; height: 1200px; overflow: hidden; }
  body { background: var(--stage); position: relative; font-family: "Arimo", Arial, sans-serif; }

  .poster {
    position: absolute; left: 40px; top: 200px;
    width: 1120px; height: 799px;
    background: var(--paper); overflow: hidden;
  }

  .hero-photo {
    position: absolute; left: 240px; top: 0; width: 880px; height: 660px;
    background:
      linear-gradient(to bottom, rgba(255,255,255,0) 55%, #fff 100%),
      linear-gradient(to right, #fff 0%, rgba(255,255,255,0) 45%),
      radial-gradient(ellipse 260px 200px at 680px 200px, var(--photo-dark) 0%, rgba(90,90,98,0.6) 55%, rgba(90,90,98,0) 100%),
      linear-gradient(135deg, var(--photo-light) 0%, var(--photo-mid) 60%, #c9c8cc 100%);
  }

  .brand { position: absolute; left: 24px; top: 28px; display: flex; align-items: center; gap: 12px; }
  .brand-square { width: 79px; height: 79px; background: var(--ink); }
  .brand-name { font-family: "Roboto", Arial, sans-serif; font-weight: 400; font-size: 33px; line-height: 36px; color: var(--ink); }

  .headline { position: absolute; left: 24px; top: 180px; color: var(--ink); font-weight: 700; }
  .headline-lead { display: block; font-size: 52px; line-height: 60px; letter-spacing: 0.5px; }
  .headline-key { display: block; font-size: 142px; line-height: 120px; letter-spacing: -2px; margin-top: -4px; }

  .values { position: absolute; left: 0; top: 416px; width: 100%; height: 240px; }
  .value { position: absolute; top: 0; width: 231px; height: 231px; border: 1.5px solid var(--ink); background: var(--paper); }
  .value-panel {
    position: absolute; inset: 6px; background: var(--ink); color: var(--text-white);
    display: flex; flex-direction: column; align-items: center;
  }
  .value-icon { margin-top: 34px; width: 70px; height: 70px; }
  .value-label { margin-top: 30px; font-size: 27px; line-height: 32px; text-align: center; font-weight: 700; }
  .value-tab { position: absolute; z-index: 2; top: 27px; left: -15px; width: 52px; height: 169px; }

  .value:nth-child(1) { left: 37px; }
  .value:nth-child(2) { left: 312px; }
  .value:nth-child(3) { left: 588px; }
  .value:nth-child(4) { left: 863px; }

  .cta-band { position: absolute; left: 0; bottom: 0; width: 100%; height: 85px; background: var(--ink); }
  .cta-rule { position: absolute; left: 27px; top: 39px; width: 600px; height: 2px; background: var(--text-white); }
  .cta-text {
    position: absolute; right: 29px; top: 18px; color: var(--text-white); white-space: nowrap;
    font-weight: 700; font-size: 34px; letter-spacing: 9px; line-height: 44px; margin-right: -9px;
  }
</style>
</head>
<body>
<main class="poster">
  <div class="hero-photo" role="img" aria-label="Softly faded photo of laboratory test equipment with an oscilloscope screen showing a signal trace"></div>

  <header class="brand">
    <div class="brand-square"></div>
    <div class="brand-name">Brindle<br>Industries</div>
  </header>

  <h1 class="headline">
    <span class="headline-lead">The Core Values of</span>
    <span class="headline-key">Quality</span>
  </h1>

  <section class="values">
    <article class="value">
      <div class="value-panel">
        <svg class="value-icon" viewBox="0 0 70 70" fill="none" stroke="#fff" stroke-width="4">
          <circle cx="30" cy="30" r="20" stroke-dasharray="7 4" stroke-width="8"/>
          <circle cx="30" cy="30" r="13"/>
          <line x1="21" y1="39" x2="39" y2="21"/>
          <circle cx="54" cy="54" r="11" fill="#fff" stroke="none"/>
          <polyline points="48,54 53,59 60,49" stroke="var(--ink)" stroke-width="3"/>
        </svg>
        <div class="value-label">Zero Defects,<br>Zero Scrap</div>
      </div>
      <svg class="value-tab" viewBox="0 0 52 169"><rect x="0" y="0" width="4" height="169" fill="var(--accent-blue)"/><polygon points="4,20 36,20 52,84 36,150 4,150" fill="var(--accent-blue)"/><text x="24" y="98" fill="#fff" font-family="Arimo, Arial, sans-serif" font-size="34" font-weight="700" text-anchor="middle">1</text></svg>
    </article>
    <article class="value">
      <div class="value-panel">
        <svg class="value-icon" viewBox="0 0 70 70" fill="#fff">
          <polygon points="35,2 37,8 43,8 38,12 40,18 35,14 30,18 32,12 27,8 33,8"/>
          <polygon points="20,8 22,13 27,13 23,16 24,21 20,18 16,21 17,16 13,13 18,13"/>
          <polygon points="50,8 52,13 57,13 53,16 54,21 50,18 46,21 47,16 43,13 48,13"/>
          <circle cx="34" cy="32" r="8"/>
          <path d="M20 56 a14 13 0 0 1 28 0 z"/>
          <circle cx="55" cy="52" r="11"/>
          <polyline points="49,52 54,57 61,47" fill="none" stroke="var(--ink)" stroke-width="3"/>
        </svg>
        <div class="value-label">Customer<br>Satisfaction</div>
      </div>
      <svg class="value-tab" viewBox="0 0 52 169"><rect x="0" y="0" width="4" height="169" fill="var(--accent-blue)"/><polygon points="4,20 36,20 52,84 36,150 4,150" fill="var(--accent-blue)"/><text x="24" y="98" fill="#fff" font-family="Arimo, Arial, sans-serif" font-size="34" font-weight="700" text-anchor="middle">2</text></svg>
    </article>
    <article class="value">
      <div class="value-panel">
        <svg class="value-icon" viewBox="0 0 70 70" fill="none" stroke="#fff" stroke-width="4">
          <path d="M56 32 A24 24 0 1 0 38 55"/>
          <polygon points="51,30 61,30 56,38" fill="#fff" stroke="none"/>
          <text x="32" y="42" fill="#fff" stroke="none" font-family="Arimo, Arial, sans-serif" font-size="28" font-weight="700" text-anchor="middle">1</text>
          <circle cx="54" cy="55" r="11" fill="#fff" stroke="none"/>
          <polyline points="48,55 53,60 60,50" stroke="var(--ink)" stroke-width="3"/>
        </svg>
        <div class="value-label">First Time<br>Right</div>
      </div>
      <svg class="value-tab" viewBox="0 0 52 169"><rect x="0" y="0" width="4" height="169" fill="var(--accent-blue)"/><polygon points="4,20 36,20 52,84 36,150 4,150" fill="var(--accent-blue)"/><text x="24" y="98" fill="#fff" font-family="Arimo, Arial, sans-serif" font-size="34" font-weight="700" text-anchor="middle">3</text></svg>
    </article>
    <article class="value">
      <div class="value-panel">
        <svg class="value-icon" viewBox="0 0 70 70" fill="#fff">
          <rect x="12" y="24" width="38" height="38"/>
          <path d="M18 24 a13 13 0 0 1 26 0 z"/>
          <path d="M25 24 v14 l6 -4 l6 4 v-14 z" fill="var(--ink)"/>
          <circle cx="54" cy="55" r="11"/>
          <polyline points="48,55 53,60 60,50" fill="none" stroke="var(--ink)" stroke-width="3"/>
        </svg>
        <div class="value-label">Product<br>Performance</div>
      </div>
      <svg class="value-tab" viewBox="0 0 52 169"><rect x="0" y="0" width="4" height="169" fill="var(--accent-blue)"/><polygon points="4,20 36,20 52,84 36,150 4,150" fill="var(--accent-blue)"/><text x="24" y="98" fill="#fff" font-family="Arimo, Arial, sans-serif" font-size="34" font-weight="700" text-anchor="middle">4</text></svg>
    </article>
  </section>

  <footer class="cta-band">
    <div class="cta-rule"></div>
    <p class="cta-text">Own Your Quality</p>
  </footer>
</main>
</body>
</html>
```